Consulting, Investors, Joint Venture Website

Founded in April 2018, Marendo Consultants Limited (MCL) is an advisory consulting firm specializing in engaging investors in business ventures in Tanzania.
With extensive experience in construction, energy, oil and gas and the legal professions, our team assembles our expertise that allows foreign investors to set foot and flourish in the Tanzanian market.
MCL is locally owned, founded and registered. Our shareholders are cultured Tanzanian citizens with extensive corporate experience in South Africa, Tanzania, United Kingdom and the United States.

Our mission is to provide responsive and unrivalled professional advice from learned and experienced professionals versed in the local market, with an understanding of the cultural and logistical challenges faced by foreign investors.

Our vision is to provide a complete investor’s package that initiates with company registration, compliance and documentation services and ultimately operational facilitation services.

Target Market(s)

Foreign Investors, International companies

Industry/Entity Type

Business Consultant

Number of Pages Required

5+ page

Requirements
Must have
• It will be 5 pages - Home, About Us, Services, Portfolio, Contact Us
Nice to have
• if it can look like https://www.plorvex.example/
• or https://www.dunetri.example or http://www.quillbrook.example/

```html
<!DOCTYPE html>
<html lang="en">
<head>
<meta charset="utf-8">
<title>Marendo Consultants Limited</title>
<link rel="stylesheet" href="https://fonts.googleapis.com/css2?family=Lato:wght@400;700;900&family=Montserrat:wght@800;900&display=swap">
<style>
:root{
  --blue:#1e5aa8;
  --blue-dark:#174a8c;
  --blue-band:#2f6fbb;
  --orange:#f7911e;
  --ink:#2a2f3a;
  --grey:#9a9a9a;
  --light:#efefef;
  --white:#ffffff;
}
*{box-sizing:border-box;margin:0;padding:0}
html,body{width:1200px;height:2553px;overflow:hidden}
body{position:relative;background:var(--white);font-family:"Lato",sans-serif;color:var(--ink)}
.abs{position:absolute}
.wide{font-family:"Montserrat",sans-serif;font-weight:900;letter-spacing:3px;text-transform:uppercase}

.topbar{left:0;top:0;width:1200px;height:41px;background:var(--blue)}
.top-social{left:96px;top:11px;display:flex;gap:14px}
.top-social span{width:18px;height:18px;border-radius:50%;background:rgba(255,255,255,.75)}
.top-mail{left:640px;top:11px;color:var(--white);font-size:16px;display:flex;align-items:center;gap:8px;white-space:nowrap}
.phone-tab{left:914px;top:0;width:208px;height:54px;background:var(--orange);border-radius:0 0 6px 6px;color:var(--white);font-weight:900;font-size:22px;display:flex;align-items:center;justify-content:center;gap:10px}

.header{left:0;top:41px;width:1200px;height:83px;background:var(--white)}
.brand{display:flex;align-items:center;gap:12px;color:var(--blue);font-weight:900;line-height:1}
.brand .mark{width:58px;height:58px;background:var(--blue)}
.brand .name{font-size:38px;letter-spacing:2px}
.brand .name small{display:block;font-size:15px;letter-spacing:7px;margin-top:4px}
.nav{top:73px;font-size:15px;color:#b0b0b0;text-transform:uppercase}
.nav.active{color:var(--blue)}

.hero{left:0;top:124px;width:1200px;height:574px;background:linear-gradient(90deg,#dde8f2 0%,#eef3f8 55%,#c9d8e6 100%)}
.hero-frame{left:77px;top:201px;width:944px;height:395px;border:3px solid var(--blue)}
.hero-title{left:141px;top:272px;font-size:48px;font-weight:900;color:var(--blue);line-height:1.2}
.hero-sub{left:141px;top:404px;width:700px;font-size:20px;font-weight:900;color:var(--ink);line-height:1.35}
.btn{display:flex;height:51px}
.btn .label{display:flex;align-items:center;justify-content:center;font-size:19px;text-transform:uppercase}
.btn .tip{width:66px;height:100%}
.btn-primary .label{background:var(--blue);color:var(--white)}
.btn-primary .tip{background:#e8eef5;border:2px solid var(--blue)}
.btn-grey .label{background:#a8a8a8;color:var(--white)}
.btn-grey .tip{background:#e6e6e6;border:2px solid #888}
.hero-person{left:850px;top:141px;width:350px;height:557px;background:linear-gradient(180deg,#9aa4ad,#6f7a86)}

.services{left:20px;top:672px;width:1160px;height:426px;background:var(--orange);box-shadow:0 4px 8px rgba(0,0,0,.25)}
.card{top:16px;width:366px}
.card .photo{width:366px;height:209px;border:2px solid var(--white)}
.card h3{margin-top:26px;font-size:19px;border-left:4px solid var(--blue);padding-left:7px;color:var(--ink);letter-spacing:2px}
.card p{margin-top:10px;font-size:14px;color:var(--ink);line-height:1.3}
.card hr{margin-top:26px;border:0;border-top:1px solid #fbc37f}
.card .more{margin-top:14px;font-size:13px;text-transform:uppercase;display:flex;justify-content:flex-end;align-items:center;gap:8px}

.welcome{left:0;top:1152px;width:1200px;text-align:center;font-size:54px;letter-spacing:4px}
.welcome .hl{color:var(--orange)}
.welcome .dk{color:var(--blue)}
.intro{left:123px;top:1232px;width:954px;text-align:center;font-size:15px;color:var(--grey);line-height:1.4}

.urgent{left:0;top:1450px;width:1200px;height:187px;background:linear-gradient(90deg,var(--blue-band),#3a78c2)}
.urgent-kicker{left:80px;top:1502px;font-size:25px;color:#b8c8da}
.urgent-title{left:80px;top:1537px;font-size:37px;font-weight:900;color:var(--white)}
.btn-white .label{background:var(--white);color:var(--blue)}
.btn-white .tip{background:#5d8fcb;border:2px solid var(--white)}

.portfolio{left:0;top:1637px;width:1200px;height:567px;background:var(--light)}
.portfolio-title{left:0;top:1697px;width:1200px;text-align:center;font-size:54px;letter-spacing:4px}
.tile{top:1777px;width:262px;height:364px}
.tile .cap{position:absolute;left:0;width:262px;height:51px;background:var(--white);font-size:15px;color:#555;text-align:center;line-height:1.25;padding:6px 22px 0}
.tile .img{position:absolute;left:0;width:262px;height:313px}
.arrow{top:1944px}

.callbar{left:0;top:2204px;width:1200px;height:106px;background:var(--orange);display:flex;align-items:center;justify-content:center;gap:10px;color:var(--white);font-size:20px}
.callbar b{font-weight:900;margin-right:18px}
.callbar a{color:var(--blue-dark);font-weight:900;font-style:italic}

.footer{left:0;top:2310px;width:1200px;height:243px;background:linear-gradient(90deg,#2c69b3,#3574bd)}
.f-head{top:2359px;font-size:19px;color:var(--white);letter-spacing:2px}
.f-text{font-size:15px;color:#c5d5e8;line-height:1.2}
.f-input{left:78px;top:2446px;width:169px;height:49px;background:var(--white);font-size:12px;color:#bbb;padding:17px 10px}
.f-tip{left:247px;top:2446px;width:64px;height:49px;background:#5d8fcb;border:2px solid var(--white)}
.f-social{top:2444px;width:44px;height:44px;border-radius:50%;border:2px solid var(--orange)}
.f-map{left:698px;top:2356px;width:146px;height:146px;border-radius:50%;border:3px solid var(--orange);background:linear-gradient(160deg,#e5ecd6,#d2dfc0)}
.f-brand{left:877px;top:2378px;color:var(--white)}
.f-brand .mark{width:44px;height:44px;background:var(--white)}
.f-brand .name{font-size:28px}
.f-brand .name small{font-size:11px;letter-spacing:6px}
.f-copy{left:877px;top:2446px;font-size:14px;color:var(--orange);font-weight:900;line-height:1.3}
.f-copy span{color:#c5d5e8;font-weight:400}
</style>
</head>
<body>

<div class="abs topbar"></div>
<div class="abs top-social"><span></span><span></span><span></span></div>
<div class="abs top-mail">
  <svg width="18" height="13" viewBox="0 0 18 13"><rect x="1" y="1" width="16" height="11" fill="none" stroke="#fff" stroke-width="1.6"/><path d="M1 1l8 6 8-6" fill="none" stroke="#fff" stroke-width="1.6"/></svg>
  info@marendoconsultants.com
</div>
<div class="abs phone-tab">
  <svg width="20" height="20" viewBox="0 0 24 24"><path d="M6.6 10.8a15 15 0 006.6 6.6l2.2-2.2a1 1 0 011-.25 11.4 11.4 0 003.6.57 1 1 0 011 1V20a1 1 0 01-1 1A17 17 0 013 4a1 1 0 011-1h3.5a1 1 0 011 1c0 1.25.2 2.45.57 3.57a1 1 0 01-.25 1z" fill="#fff"/></svg>
  123 456 7878
</div>

<div class="abs header"></div>
<div class="abs brand" style="left:77px;top:52px">
  <div class="mark"></div>
  <div class="name">MARENDO<small>CONSULTANTS</small></div>
</div>
<div class="abs nav active" style="left:618px">Home</div>
<div class="abs nav" style="left:698px">About Us</div>
<div class="abs nav" style="left:808px">Services</div>
<div class="abs nav" style="left:911px">Portfolio</div>
<div class="abs nav" style="left:1025px">Contact Us</div>

<div class="abs hero" role="img" aria-label="Misty city skyline of office towers"></div>
<div class="abs hero-frame"></div>
<div class="abs hero-person" role="img" aria-label="Smiling businesswoman with folded arms"></div>
<h1 class="abs hero-title">PROFESSIONAL CONSULTING<br>FOR YOUR BUSINESS</h1>
<p class="abs hero-sub">Being professionals in business consulting for over adecade, we use our experience at its fullest for your business to prosper.</p>
<div class="abs btn btn-primary" style="left:140px;top:475px"><span class="label" style="width:209px">Get Started Now</span><span class="tip"></span></div>
<div class="abs btn btn-grey" style="left:436px;top:475px"><span class="label" style="width:146px">Learn More</span><span class="tip"></span></div>

<section class="abs services">
  <div class="abs card" style="left:16px">
    <div class="photo" role="img" aria-label="Team meeting around a table with laptops" style="background:linear-gradient(135deg,#8e9aa6,#cfd6dc)"></div>
    <h3 class="wide">Why Our Consulting</h3>
    <p>Our team assembles our expertise that allows foreign investors to set foot and flourish.</p>
    <hr>
    <div class="more"><svg width="26" height="10" viewBox="0 0 26 10"><path d="M0 5h23M19 1l5 4-5 4" fill="none" stroke="#2a2f3a" stroke-width="1.8"/></svg>Read More</div>
  </div>
  <div class="abs card" style="left:397px">
    <div class="photo" role="img" aria-label="Businessman reading a tablet outdoors" style="background:linear-gradient(135deg,#d9cdb4,#a9a196)"></div>
    <h3 class="wide">Variety of Services</h3>
    <p>Marendo Consultants has a long history of experience across a wide range of services.</p>
    <hr>
    <div class="more"><svg width="26" height="10" viewBox="0 0 26 10"><path d="M0 5h23M19 1l5 4-5 4" fill="none" stroke="#2a2f3a" stroke-width="1.8"/></svg>Read More</div>
  </div>
  <div class="abs card" style="left:777px">
    <div class="photo" role="img" aria-label="Advisor reviewing documents with a couple" style="background:linear-gradient(135deg,#c8ced4,#7d8b99)"></div>
    <h3 class="wide">Planing Your Future</h3>
    <p>We propose a number of solutions for your issues, calculating the future possibilities.</p>
    <hr>
    <div class="more"><svg width="26" height="10" viewBox="0 0 26 10"><path d="M0 5h23M19 1l5 4-5 4" fill="none" stroke="#2a2f3a" stroke-width="1.8"/></svg>Read More</div>
  </div>
</section>

<h2 class="abs welcome wide"><span class="dk">Welcome</span> <span class="hl">to Marendo</span></h2>
<p class="abs intro">Lorem Ipsum is simply dummy text of the printing and typesetting industry. Lorem Ipsum has been the industry's standard dummy text ever since the 1500s, when an unknown printer took a galley of type and scrambled it to make a type specimen book. It has survived not only five centuries, but also the leap into electronic typesetting, remaining essentially unchanged. It was popularised in the 1960s with the release of Letraset sheets containing Lorem Ipsum passages.</p>
<div class="abs btn btn-primary" style="left:488px;top:1336px"><span class="label" style="width:155px">Learn More</span><span class="tip"></span></div>

<div class="abs urgent" role="img" aria-label="Blurred handshake in blue tones"></div>
<div class="abs urgent-kicker wide">Have an urgent need in a</div>
<div class="abs urgent-title">PROFESSIONAL BUSINESS CONSULTANT?</div>
<div class="abs btn btn-white" style="left:887px;top:1518px"><span class="label" style="width:167px">Join Us Now</span><span class="tip"></span></div>

<section class="abs portfolio"></section>
<h2 class="abs portfolio-title wide"><span style="color:var(--blue)">Our</span> <span style="color:var(--orange)">Portfolio</span></h2>
<div class="abs tile" style="left:77px">
  <div class="cap" style="top:0">Lorem Ipsum is simply dummy text of the printing.</div>
  <div class="img" style="top:51px;background:linear-gradient(160deg,#d8dde2,#5b6670)" role="img" aria-label="Business team discussing at a table"></div>
</div>
<div class="abs tile" style="left:339px">
  <div class="img" style="top:0;background:linear-gradient(180deg,#2b4a78,#6f8fb3 55%,#24416c)" role="img" aria-label="Industrial plant reflected in water at dusk"></div>
  <div class="cap" style="top:313px">Lorem Ipsum is simply dummy text of the printing.</div>
</div>
<div class="abs tile" style="left:601px">
  <div class="cap" style="top:0">Lorem Ipsum is simply dummy text of the printing.</div>
  <div class="img" style="top:51px;background:linear-gradient(180deg,#5f86ad,#6f8a58 60%,#3f4a3c)" role="img" aria-label="Tanker truck on a highway"></div>
</div>
<div class="abs tile" style="left:863px">
  <div class="img" style="top:0;background:linear-gradient(180deg,#9fc4e8,#1d5aa6)" role="img" aria-label="Offshore oil platform at sea"></div>
  <div class="cap" style="top:313px">Lorem Ipsum is simply dummy text of the printing.</div>
</div>
<svg class="abs arrow" style="left:30px" width="16" height="28" viewBox="0 0 16 28"><path d="M14 2L3 14l11 12" fill="none" stroke="#555" stroke-width="2"/></svg>
<svg class="abs arrow" style="left:1152px" width="16" height="28" viewBox="0 0 16 28"><path d="M2 2l11 12L2 26" fill="none" stroke="#555" stroke-width="2"/></svg>

<div class="abs callbar">
  <svg width="20" height="20" viewBox="0 0 24 24"><path d="M6.6 10.8a15 15 0 006.6 6.6l2.2-2.2a1 1 0 011-.25 11.4 11.4 0 003.6.57 1 1 0 011 1V20a1 1 0 01-1 1A17 17 0 013 4a1 1 0 011-1h3.5a1 1 0 011 1c0 1.25.2 2.45.57 3.57a1 1 0 01-.25 1z" fill="#2a2f3a"/></svg>
  Call Us On : <b>123 456 7878</b> or Request a Quote on our mail id <a>info@marendoconsultants.com</a>
</div>

<footer class="abs footer" role="img" aria-label="Faint blue cityscape behind the footer"></footer>
<div class="abs f-head wide" style="left:80px">Newsletter</div>
<p class="abs f-text" style="left:80px;top:2393px;width:340px">Join Marendo Consultants Business to Get Latest News &amp; Updates.</p>
<div class="abs f-input">Email</div>
<div class="abs f-tip"></div>

<div class="abs f-head wide" style="left:456px">Contact Us</div>
<svg class="abs" style="left:456px;top:2396px" width="16" height="22" viewBox="0 0 16 22"><path d="M8 0a8 8 0 00-8 8c0 6 8 14 8 14s8-8 8-14a8 8 0 00-8-8z" fill="#f7911e"/><circle cx="8" cy="8" r="3" fill="#2f6fbb"/></svg>
<p class="abs f-text" style="left:485px;top:2393px;width:200px;color:var(--white)">123,Loprem ipsum dummy City, Country 123456.</p>
<div class="abs f-social" style="left:455px;background:var(--white)"></div>
<div class="abs f-social" style="left:507px"></div>
<div class="abs f-social" style="left:558px"></div>

<div class="abs f-map" role="img" aria-label="Location map"></div>

<div class="abs brand f-brand">
  <div class="mark"></div>
  <div class="name">MARENDO<small>CONSULTANTS</small></div>
</div>
<p class="abs f-copy">© MARENDO CONSULTANTS<br><span>- 2018. All Rights Reserved</span></p>

</body>
</html>
```